Institutional website for an IT Consulting company

Web design + HTML + CSS / Bootstrap + JS (interaction) integration in order to extend our existing website brisklane.coop.
Our website is currently aiming only for recruitment and not for customers, we want to provide a fluid transition between customer side website (this project) and recruitment website (existing site).

Ideally we would love the new design to be "inspired" by our actual graphic chart (Colors mainly). It should provide a great user experience and a landing page (or any mean) allowing the visitor to easily switch from the end customer front end (this project), the recruitment front end (existing front end https://www.brisklane.coop/) and the existing member front end (an other existing front end dedicated to members already existing).

In attachment you will find the expected site content mainly a one page with a first level of information and "link" to sub pages (a way to directly access this sub pages should also be provided).

The website should be accessible on mobile device and desktop.

The attachment is in french as it reflect the final site content, but if google translate isn't sufficient to have a general idea of the content, feel free to ask. We would love to have some visual representation for some categories.

Target Market(s)

fortune 500 companies

Industry/Entity Type

It Company

Coding

Coded - Design and coding required

Number of Pages Required

5+ page

Requirements
Must have
• This project must have an easy way to navigate between 3 sub sites, the customer one (the one designed here), the consultant / recruitment one (the existing one at brisklane.coop), the members one.

A one page experience at first leading to detail pages.

Custom made visuals to illustrate each categories.

Inspiration websites : plovu[.]fr ; tarnsby[.]com ; qolvari[.] com ...

Be inspired by the existing color from our logo and existing website at brisklane[.]coop

```html
<!DOCTYPE html>
<html lang="en">
<head>
<meta charset="utf-8">
<title>Brisklane.coop – IT Consulting</title>
<link rel="stylesheet" href="https://fonts.googleapis.com/css2?family=Oswald:wght@400;500&family=Nunito:wght@400;600;700&display=swap">
<style>
:root{
  --teal:#17b1b6;
  --teal-dark:#0f8f94;
  --mint:#dcf6f2;
  --mint-soft:#e3f8f4;
  --paper:#f8f8f8;
  --ink:#222a2c;
  --muted:#4a4f52;
  --line:#d6dadb;
  --footer:#3d3f40;
  --white:#ffffff;
}
*{box-sizing:border-box;margin:0;padding:0}
html,body{width:1200px;height:4897px;overflow:hidden}
body{font-family:"Nunito",sans-serif;color:var(--ink);background:var(--white);position:relative}
.abs{position:absolute}
section,footer{position:absolute;left:0;width:1200px}
.heading{font-family:"Oswald",sans-serif;font-weight:500;font-size:35px;letter-spacing:.3px;color:var(--ink);text-align:center;width:1200px;left:0}
.teal-link{color:var(--teal);font-weight:700;font-size:17px;text-decoration:none;display:flex;align-items:center;gap:22px}
.body-text{font-size:15px;line-height:24px;color:var(--muted)}
.body-text a{color:var(--teal);text-decoration:none}
.photo{border-radius:22px}

/* hero */
.hero{top:0;height:570px;background:var(--mint)}
.logo{left:59px;top:34px;font-family:"Nunito",sans-serif;font-weight:700;font-size:30px;color:var(--teal-dark);letter-spacing:1px;display:flex;align-items:flex-end;gap:4px}
.logo small{font-size:11px;margin-bottom:6px;letter-spacing:0}
.btn{height:42px;border-radius:4px;font-size:13px;display:flex;align-items:center;justify-content:center}
.btn-outline{left:784px;top:32px;width:146px;border:1.5px solid var(--muted);color:var(--muted)}
.btn-fill{left:960px;top:32px;width:179px;background:var(--teal);color:var(--white)}
.hero-title{left:59px;top:258px;font-family:"Oswald",sans-serif;font-weight:500;font-size:35px;line-height:45px;color:var(--ink)}
.search{left:59px;top:378px;width:280px;height:44px;border:1.5px solid #9aa3a5;border-radius:4px;background:var(--mint);font-size:13px;color:#8a9294;padding:13px 16px}
.search-btn{left:359px;top:378px;width:145px;height:44px;background:var(--teal);color:var(--white);border-radius:4px;font-size:14px;display:flex;align-items:center;justify-content:center}
.hero-person{left:751px;top:114px;width:266px;height:456px;border-radius:120px 120px 0 0;background:linear-gradient(180deg,#c9a78a 0%,#a9b0bd 35%,#7d8796 100%)}

/* provider */
.provider{top:570px;height:562px;background:var(--paper)}
.provider .heading{top:64px}
.provider-photo{left:74px;top:168px;width:437px;height:331px;background:linear-gradient(135deg,#dfe5e3,#8d9a99 55%,#4d5857)}
.provider-text{left:569px;top:215px;width:570px}

/* subjects */
.subjects{top:1132px;height:590px;background:linear-gradient(180deg,#eae5df 0%,#f3efe9 45%,#d9cdc2 100%);overflow:hidden}
.subjects .heading{top:62px}
.arrow-btn{width:30px;height:30px;border:1.5px solid var(--ink);border-radius:50%;display:flex;align-items:center;justify-content:center}
.subject-card{top:186px;width:245px;height:274px;background:var(--white);border-radius:6px}
.subject-card .icon{position:absolute;left:76px;top:62px;width:92px;height:92px;border:3px solid var(--teal);border-radius:50%;display:flex;align-items:center;justify-content:center}
.subject-card .rule{position:absolute;left:0;top:184px;width:100%;height:2px;background:var(--teal)}
.subject-card .label{position:absolute;left:0;top:206px;width:100%;text-align:center;font-family:"Oswald",sans-serif;font-size:17px;line-height:26px;color:var(--ink)}
.subject-links{top:510px;font-size:17px;font-weight:700;color:var(--ink);display:flex;align-items:center;gap:6px}
.subject-links svg{margin-top:2px}

/* scop */
.scop{top:1722px;height:637px;background:var(--white)}
.scop .heading{top:68px}
.scop-card{top:167px;width:340px}
.scop-card .img{width:340px;height:228px;border-radius:10px}
.scop-card h3{margin-top:22px;font-family:"Oswald",sans-serif;font-weight:500;font-size:21px;color:var(--ink)}
.scop-card p{margin-top:12px;height:72px}
.scop-card .teal-link{margin-top:16px}

/* experts */
.experts{top:2359px;height:956px;background:var(--mint-soft)}
.experts .heading{top:68px}
.experts-text{width:490px}
.feature{display:flex;align-items:center;gap:14px;font-size:15px;color:var(--muted)}
.experts-photo-a{left:664px;top:154px;width:437px;height:331px;background:linear-gradient(135deg,#e8eef2,#b9c6cf 50%,#50606b)}
.experts-photo-b{left:97px;top:561px;width:437px;height:331px;background:linear-gradient(135deg,#f0ece6,#b3b7bb 50%,#3e4a55)}

/* news */
.news{top:3315px;height:508px;background:var(--paper)}
.news .heading{top:68px}
.news-item{top:166px;width:264px}
.news-item .img{width:264px;height:186px}
.news-item p{margin-top:28px;font-size:15px;line-height:24px;font-weight:600;color:var(--ink)}

/* testimonials */
.testimonials{top:3823px;height:662px;background:var(--mint-soft)}
.testimonials .heading{top:70px}
.testi-card{left:145px;top:171px;width:911px;height:405px;background:var(--white);border-radius:16px}
.client{left:59px;top:38px;display:flex;align-items:center;gap:22px;font-family:"Oswald",sans-serif;font-size:26px;color:var(--ink)}
.client-mark{width:50px;height:50px;background:var(--ink);border-radius:4px}
.client .sep{color:#9aa0a3;font-weight:400}
.testi-photo{left:55px;top:129px;width:245px;height:147px;border-radius:6px;background:linear-gradient(135deg,#1f3550,#3a6d9a 55%,#152234)}
.testi-text{left:353px;top:152px;width:520px}
.testi-quote{left:55px;top:307px;width:820px;font-size:16px;line-height:24px;font-weight:600;color:var(--teal)}

/* footer */
.footer{top:4485px;height:412px;background:var(--footer);color:var(--white)}
.footer-col{top:72px}
.footer-col h4{font-family:"Oswald",sans-serif;font-weight:500;font-size:22px;margin-bottom:20px}
.footer-col li{list-style:none;font-size:16px;line-height:32px}
.footer-rule{left:0;top:320px;width:1200px;height:1px;background:#5c5f60}
.footer-bottom{top:353px;font-size:16px}
.to-top{left:587px;top:351px;width:26px;height:26px;border:1.5px solid var(--teal);display:flex;align-items:center;justify-content:center}
</style>
</head>
<body>

<section class="hero">
  <div class="abs logo">BRISKLANE<small>.coop</small></div>
  <div class="abs btn btn-outline">I am Brisklane</div>
  <div class="abs btn btn-fill">I want to join Brisklane</div>
  <h1 class="abs hero-title">Our Expert Consultants Can Make<br>Your Company Achieve Results</h1>
  <div class="abs search">Search Profiles</div>
  <div class="abs search-btn">Search</div>
  <div class="abs hero-person" role="img" aria-label="Smiling consultant in a grey blazer holding an open laptop"></div>
</section>

<section class="provider">
  <h2 class="abs heading">An Expert Service Provider</h2>
  <div class="abs photo provider-photo" role="img" aria-label="Developers working at computers in a bright office"></div>
  <p class="abs body-text provider-text">Brisklane:coop is a services company with strong values &amp;cooperation, based in particular on an atypical management <a href="#">View CAE Scop</a><br>We have independent profiles on Si such as Cirrane DI, infrastructure and secunty, Data Platform <a href="#">Search</a><br>But why should you chose only one consultant when Brisklane:coop can suggest a whole community to your service!<br>Brisklane is first and foremost a team of experts <a href="#">Go to Experts Domain</a><br>&nbsp;including also a few MVPs in cooperation with the group of consultants on a dal., hams. Our teams are highly oriented on cirrane topics; Data Platform, Data &amp; BI</p>
</section>

<section class="subjects" role="img" aria-label="Blurred background of colleagues in a meeting room">
  <h2 class="abs heading">We can Intervene in the Following Subjects</h2>
  <div class="abs arrow-btn" style="left:101px;top:133px"><svg width="12" height="12" viewBox="0 0 12 12"><path d="M8 2 4 6l4 4" fill="none" stroke="#222a2c" stroke-width="1.6"/></svg></div>
  <div class="abs arrow-btn" style="left:147px;top:133px"><svg width="12" height="12" viewBox="0 0 12 12"><path d="M4 2l4 4-4 4" fill="none" stroke="#222a2c" stroke-width="1.6"/></svg></div>

  <div class="abs subject-card" style="left:97px">
    <div class="icon"><svg width="50" height="50" viewBox="0 0 50 50" fill="none" stroke="#17b1b6" stroke-width="2"><circle cx="12" cy="8" r="4"/><circle cx="25" cy="8" r="4"/><circle cx="38" cy="8" r="4"/><path d="M12 12v6h26v-6M25 12v8"/><ellipse cx="25" cy="24" rx="10" ry="4"/><path d="M15 24v16c0 2 4.5 4 10 4s10-2 10-4V24M15 32c0 2 4.5 4 10 4s10-2 10-4"/></svg></div>
    <div class="rule"></div><div class="label">Hybrid architecture</div>
  </div>
  <div class="abs subject-card" style="left:359px">
    <div class="icon"><svg width="50" height="50" viewBox="0 0 50 50" fill="none" stroke="#17b1b6" stroke-width="2"><rect x="7" y="12" width="36" height="24" rx="2"/><path d="M19 44h12M25 36v8"/><rect x="19" y="18" width="12" height="11"/><path d="M21 18v-3a4 4 0 0 1 8 0v3M25 22v3"/></svg></div>
    <div class="rule"></div><div class="label">Security &amp; Infrastructure</div>
  </div>
  <div class="abs subject-card" style="left:622px">
    <div class="icon"><svg width="50" height="50" viewBox="0 0 50 50" fill="none" stroke="#17b1b6" stroke-width="2"><path d="M15 20a8 8 0 0 1 15-5 6 6 0 0 1 6 9H15a5 5 0 0 1 0-4z"/><ellipse cx="25" cy="30" rx="7" ry="3"/><path d="M18 30v10c0 1.5 3 3 7 3s7-1.5 7-3V30M18 35c0 1.5 3 3 7 3s7-1.5 7-3"/></svg></div>
    <div class="rule"></div><div class="label">Expertise on Modern<br>Data Warehouse</div>
  </div>
  <div class="abs subject-card" style="left:884px">
    <div class="icon"><svg width="50" height="50" viewBox="0 0 50 50" fill="none" stroke="#17b1b6" stroke-width="2"><rect x="9" y="8" width="26" height="34" rx="2"/><path d="M14 15h16M14 21h10"/><circle cx="33" cy="33" r="8"/><path d="M33 29v4l3 2"/></svg></div>
    <div class="rule"></div><div class="label">Cost rationalisation<br>on Cirrane</div>
  </div>
  <div class="abs subject-card" style="left:1147px"><div class="rule"></div></div>

  <div class="abs subject-links" style="left:264px">I have a Question <svg width="14" height="14" viewBox="0 0 14 14"><path d="M3 11 11 3M5 3h6v6" fill="none" stroke="#17b1b6" stroke-width="2"/></svg></div>
  <div class="abs subject-links" style="left:544px">Need More Info <svg width="14" height="14" viewBox="0 0 14 14"><path d="M3 11 11 3M5 3h6v6" fill="none" stroke="#17b1b6" stroke-width="2"/></svg></div>
  <div class="abs subject-links" style="left:782px">Contatc us <svg width="14" height="14" viewBox="0 0 14 14"><path d="M3 11 11 3M5 3h6v6" fill="none" stroke="#17b1b6" stroke-width="2"/></svg></div>
</section>

<section class="scop">
  <h2 class="abs heading">Brisklane CAE-Scop</h2>
  <article class="abs scop-card" style="left:59px">
    <div class="img" role="img" aria-label="Consultant in a suit working at a desk" style="background:linear-gradient(135deg,#eef1f2,#a8b2b7 55%,#2c3338)"></div>
    <h3>Custom-made S/E</h3>
    <p class="body-text">According to your needs our consultants will be able to&nbsp; assist you in achieving your projects</p>
    <a class="teal-link" href="#">Find out more <svg width="12" height="12" viewBox="0 0 12 12"><path d="M2 10 10 2M4 2h6v6" fill="none" stroke="#222a2c" stroke-width="2"/></svg></a>
  </article>
  <article class="abs scop-card" style="left:430px">
    <div class="img" role="img" aria-label="Team gathered around a whiteboard with sticky notes" style="background:linear-gradient(135deg,#d9d4cc,#8d8178 50%,#3b3531)"></div>
    <h3>A Team At Your Service</h3>
    <p class="body-text">We work not only in consultant to customer mode but from community to customer mode.</p>
    <a class="teal-link" href="#">Find out more <svg width="12" height="12" viewBox="0 0 12 12"><path d="M2 10 10 2M4 2h6v6" fill="none" stroke="#222a2c" stroke-width="2"/></svg></a>
  </article>
  <article class="abs scop-card" style="left:801px">
    <div class="img" role="img" aria-label="Hands with a calculator and documents on a desk" style="background:linear-gradient(135deg,#5a4a40,#cfc7bd 55%,#8f857c)"></div>
    <h3>A Fair Pay</h3>
    <p class="body-text">At brisklane S/E directly gain for what they work for.</p>
    <a class="teal-link" href="#">Find out more <svg width="12" height="12" viewBox="0 0 12 12"><path d="M2 10 10 2M4 2h6v6" fill="none" stroke="#222a2c" stroke-width="2"/></svg></a>
  </article>
</section>

<section class="experts">
  <h2 class="abs heading">Experts in their field</h2>
  <p class="abs body-text experts-text" style="left:91px;top:214px">S/E eexports are able to assist you on each standard phase of a data platform project.We also offer Formal or custom training but also the capacity of purchasing cirrane credits or Q365 licences.</p>
  <div class="abs feature" style="left:91px;top:328px"><svg width="34" height="30" viewBox="0 0 34 30" fill="none" stroke="#4a4f52" stroke-width="1.5"><path d="M2 28h30M6 28V18h5v10M14 28V13h5v15M22 28V8h5v20M4 12 14 5l6 4 10-7"/></svg>Data Platform project</div>
  <div class="abs feature" style="left:335px;top:328px"><svg width="34" height="30" viewBox="0 0 34 30" fill="none" stroke="#4a4f52" stroke-width="1.5"><path d="M2 28h30M6 28V18h5v10M14 28V13h5v15M22 28V8h5v20M4 12 14 5l6 4 10-7"/></svg>Cloud Solution Provider</div>
  <div class="abs feature" style="left:91px;top:388px"><svg width="34" height="32" viewBox="0 0 34 32" fill="none" stroke="#4a4f52" stroke-width="1.5"><circle cx="17" cy="13" r="10"/><circle cx="17" cy="13" r="5"/><path d="M11 21l-3 9 5-2 3 3M23 21l3 9-5-2-3 3"/></svg>Training</div>
  <div class="abs photo experts-photo-a" role="img" aria-label="Consultant presenting a diagram on a whiteboard"></div>

  <div class="abs photo experts-photo-b" role="img" aria-label="Group of smiling colleagues standing together in an office"></div>
  <p class="abs body-text experts-text" style="left:630px;top:596px">In order to find and directly contact the profile(s) that is/are best suited to your needs, please use our research tool. The customer relationship team is also available to answer to all you inquiries</p>
  <div class="abs feature" style="left:626px;top:712px"><svg width="34" height="32" viewBox="0 0 34 32" fill="none" stroke="#4a4f52" stroke-width="1.5"><rect x="4" y="3" width="22" height="26" rx="2"/><path d="M9 10h12M9 15h12M9 20h6"/><circle cx="26" cy="22" r="5"/></svg>Certifications</div>
  <div class="abs feature" style="left:884px;top:712px"><svg width="34" height="32" viewBox="0 0 34 32" fill="none" stroke="#4a4f52" stroke-width="1.5"><rect x="10" y="3" width="20" height="26" rx="2"/><path d="M15 10h10M15 15h10"/><circle cx="10" cy="20" r="6"/><path d="M7 25l-2 5 5-2 5 2-2-5"/></svg>Most Valuable Professional</div>
  <div class="abs feature" style="left:626px;top:771px"><svg width="34" height="32" viewBox="0 0 34 32" fill="none" stroke="#4a4f52" stroke-width="1.5"><path d="M5 8l12-5 12 5-12 5z"/><path d="M10 11v5c0 3 14 3 14 0v-5"/><path d="M8 30c0-6 4-9 9-9s9 3 9 9"/></svg>Veltrix Certified Trainer</div>
  <div class="abs feature" style="left:884px;top:771px"><svg width="34" height="32" viewBox="0 0 34 32" fill="none" stroke="#4a4f52" stroke-width="1.5"><circle cx="17" cy="9" r="6"/><path d="M6 30c0-7 5-11 11-11s11 4 11 11"/><circle cx="17" cy="24" r="3"/></svg>Gold Partners</div>
  <a class="abs teal-link" href="#" style="left:621px;top:831px">Contact us <svg width="12" height="12" viewBox="0 0 12 12"><path d="M2 10 10 2M4 2h6v6" fill="none" stroke="#17b1b6" stroke-width="2"/></svg></a>
</section>

<section class="news">
  <h2 class="abs heading">Latest News</h2>
  <article class="abs news-item" style="left:59px">
    <div class="img" role="img" aria-label="Two people talking in lounge chairs by tall windows" style="background:linear-gradient(180deg,#dfe6ea,#b8c3c9 60%,#6d7a80)"></div>
    <p>New Gold certification obtained in july 2020</p>
  </article>
  <article class="abs news-item" style="left:333px">
    <div class="img" role="img" aria-label="Glowing fibre optic cables in a server rack" style="background:linear-gradient(135deg,#1b2a44,#b9783a 55%,#16213a)"></div>
    <p>&nbsp;&nbsp;Evolution of the number of certification obtained by our consultants</p>
  </article>
  <article class="abs news-item" style="left:605px">
    <div class="img" role="img" aria-label="Computer monitor glowing in a dark office" style="background:linear-gradient(135deg,#0f2b35,#2f6b78 55%,#0b1c22)"></div>
    <p>&nbsp;&nbsp;Arrival of a new consultant/ support function</p>
  </article>
  <article class="abs news-item" style="left:879px">
    <div class="img" role="img" aria-label="Two people talking in lounge chairs by tall windows" style="background:linear-gradient(180deg,#dfe6ea,#b8c3c9 60%,#6d7a80)"></div>
    <p>Weekend / day/ half-day between Brisklane. Show our cooperative side, cohesive team</p>
  </article>
</section>

<section class="testimonials">
  <h2 class="abs heading">Testimonials</h2>
  <div class="abs arrow-btn" style="left:62px;top:354px"><svg width="12" height="12" viewBox="0 0 12 12"><path d="M8 2 4 6l4 4" fill="none" stroke="#222a2c" stroke-width="1.6"/></svg></div>
  <div class="abs arrow-btn" style="left:1108px;top:354px"><svg width="12" height="12" viewBox="0 0 12 12"><path d="M4 2l4 4-4 4" fill="none" stroke="#222a2c" stroke-width="1.6"/></svg></div>
  <div class="abs testi-card">
    <div class="abs client"><span class="client-mark"></span><span>Streamora <span class="sep">|</span> Security Upgrade Project</span></div>
    <div class="abs testi-photo" role="img" aria-label="Engineer with a laptop in a server room"></div>
    <p class="abs body-text testi-text">S/E exports are able to assist you on each standard phase of a data platform project. We also offer formal or custom training but also the capacity of purchasing Cirrane credits or Q365 licences.</p>
    <p class="abs testi-quote">"The brisklane is not just about a consultant and you, its about the whole community. They offer formal or custom training but also the capacity of purchasing Cirrane credits or Q365 licences."</p>
  </div>
</section>

<footer class="footer">
  <div class="abs footer-col" style="left:61px"><h4>Company</h4><ul><li>About Us</li><li>Services</li><li>How it works</li><li>Contact</li></ul></div>
  <div class="abs footer-col" style="left:331px"><h4>Product</h4><ul><li>Contractors</li><li>Current Jobs</li><li>Testimonials</li><li>Affiliate</li></ul></div>
  <div class="abs footer-col" style="left:610px"><h4>Support</h4><ul><li>FAQS</li><li>Customers support</li><li>Help</li></ul></div>
  <div class="abs footer-col" style="left:871px"><h4>Other</h4><ul><li>Profile</li><li>Dashboard</li><li>Blog</li></ul></div>
  <div class="abs footer-rule"></div>
  <div class="abs footer-bottom" style="left:61px">Privacy Policy&nbsp;&nbsp;&nbsp;User Agreement</div>
  <div class="abs to-top"><svg width="12" height="10" viewBox="0 0 12 10"><path d="M2 8l4-5 4 5" fill="none" stroke="#17b1b6" stroke-width="1.8"/></svg></div>
  <div class="abs footer-bottom" style="left:912px">All Rights Reserved © 2020</div>
</footer>

</body>
</html>
```